Verdant Drops Supply Product Labels

Hi, I need to have a label designed for my organic essential oil company You completed TLV Solutions for me and I was very happy with the design. TLV is for preparing plans for business restructures but I am launching a website for my real project which is selling organic essential oils. I am seeking a very simple design and have a clear idea of the look, design and style. Same design but for several sizes (bottles) plus labels for packaging. Check out my Facebook page Verdant Drops Supply

Industry/Entity Type

It Company

Font styles to use
Serif

Requirements
Must have
• Be simple, clean, black and white design. I have logo and examples of designs.

```html
<!DOCTYPE html>
<html lang="en">
<head>
<meta charset="utf-8">
<title>Verdant Drops Supply – Wild Lavender Labels</title>
<link rel="stylesheet" href="https://fonts.googleapis.com/css2?family=Nunito:wght@300;400;600;700&display=swap">
<style>
  :root {
    --page: #ffffff;
    --ink: #111111;
    --ink-soft: #3a3a3a;
    --brand-grey: #6f7378;
    --paper-dark: #a9abad;
    --paper-mid: #e2e3e4;
    --paper-light: #fafafa;
    --band: #0d0d0d;
    --rule: #2a2a2a;
    --on-dark: #f2f2f2;
    --on-dark-soft: #b9b9b9;
  }
  * { box-sizing: border-box; margin: 0; padding: 0; }
  html, body {
    width: 1200px; height: 808px; overflow: hidden;
    background: var(--page);
    font-family: "Nunito", Arial, sans-serif;
    color: var(--ink);
  }
  .label-set {
    position: relative; width: 1200px; height: 808px;
    display: flex; justify-content: center; align-items: center; gap: 75px;
  }
  .label {
    position: relative; width: 300px; height: 440px;
    background: linear-gradient(90deg, var(--paper-dark) 0%, var(--paper-mid) 22%, var(--paper-light) 50%, var(--paper-mid) 78%, var(--paper-dark) 100%);
    display: flex; flex-direction: column; align-items: center;
    text-align: center; overflow: hidden;
  }
  .brand-name {
    font-size: 17px; font-weight: 600; color: var(--brand-grey);
    letter-spacing: 0.3px; line-height: 1.2;
  }
  .category {
    font-size: 11px; font-weight: 600; letter-spacing: 1.2px; color: var(--ink-soft);
  }
  .rule { width: 200px; height: 2px; background: var(--rule); }
  .product-name {
    font-size: 29px; font-weight: 300; letter-spacing: 0.5px; line-height: 1;
  }
  .product-name strong { font-weight: 600; }
  .botanical { font-size: 14px; font-weight: 400; color: var(--ink-soft); }
  .volume {
    position: absolute; left: 0; right: 0;
    font-size: 8px; font-weight: 600; letter-spacing: 0.5px; color: var(--ink-soft);
  }

  /* Variant one: silver with black edge bands */
  .label--classic { border-top: 5px solid var(--band); }
  .label--classic::after {
    content: ""; position: absolute; left: 0; right: 0; bottom: 0; height: 14px;
    background: var(--band);
  }
  .label--classic .brand-name { margin-top: 78px; }
  .label--classic .rule { margin-top: 48px; }
  .label--classic .category { margin-top: 10px; }
  .label--classic .product-name { margin-top: 32px; }
  .label--classic .botanical { margin-top: 14px; }
  .label--classic .volume { bottom: 24px; }

  /* Variant two: silver head, black body */
  .label--split .brand-name { margin-top: 78px; }
  .label--split .dark-panel {
    position: absolute; left: 0; right: 0; top: 148px; bottom: 0;
    background: var(--band); color: var(--on-dark);
    display: flex; flex-direction: column; align-items: center;
  }
  .label--split .category { color: var(--on-dark); margin-top: 22px; }
  .label--split .rule { background: var(--on-dark-soft); margin-top: 18px; height: 1px; }
  .label--split .product-name { margin-top: 16px; }
  .label--split .botanical { color: var(--on-dark-soft); margin-top: 14px; }
  .label--split .volume { bottom: 12px; color: var(--on-dark-soft); }

  /* Variant three: seal mark with pill tag */
  .label--seal .seal { margin-top: 34px; }
  .label--seal .brand-name { margin-top: 10px; color: var(--ink); font-size: 15px; }
  .label--seal .product-name { margin-top: 60px; }
  .label--seal .botanical { margin-top: 12px; }
  .label--seal .pill {
    position: absolute; left: 50%; transform: translateX(-50%); bottom: 58px;
    background: var(--band); color: var(--on-dark);
    padding: 6px 14px; border-radius: 7px;
    font-size: 12px; font-weight: 600; letter-spacing: 1px;
  }
  .label--seal .volume { bottom: 26px; }
</style>
</head>
<body>
  <main class="label-set">
    <section class="label label--classic">
      <p class="brand-name">Verdant Drops Supply</p>
      <div class="rule"></div>
      <p class="category">PURE ESSENTIAL OIL</p>
      <h2 class="product-name">WILD <strong>LAVENDER</strong></h2>
      <p class="botanical">Lavendula Angustifolia</p>
      <p class="volume">18 OZ</p>
    </section>

    <section class="label label--split">
      <p class="brand-name">Verdant Drops Supply</p>
      <div class="dark-panel">
        <p class="category">PURE ESSENTIAL OIL</p>
        <div class="rule"></div>
        <h2 class="product-name">WILD <strong>LAVENDER</strong></h2>
        <p class="botanical">Lavendula Angustifolia</p>
        <p class="volume">18 OZ</p>
      </div>
    </section>

    <section class="label label--seal">
      <svg class="seal" width="64" height="64" viewBox="0 0 64 64" aria-hidden="true">
        <circle cx="32" cy="32" r="31" fill="#111111"/>
      </svg>
      <p class="brand-name">Verdant Drops Supply</p>
      <h2 class="product-name">WILD <strong>LAVENDER</strong></h2>
      <p class="botanical">Lavendula Angustifolia</p>
      <p class="pill">PURE ESSENTIAL OIL</p>
      <p class="volume">18 OZ</p>
    </section>
  </main>
</body>
</html>
```